Banners for Project Management Conference Social Media SItes

We are part of an established global professional project management organisation (ZRV.org). We would be having our 21st project management conference in New Zealand this year and we are looking at a design of a series of banners that can be used across chatterly, blipster and workmesh. The design of banners should express the theme of the conference, "Shaping the Future".

Our conference logo is as attached. The conference logo must be in the banner image and form part of the inspiration to the banner design.

The banners fitting chatterly, blipster and workmesh should adhere to the banner sizing as follows.

1500x500px Blipster banner
851x315px Chatterly banner
646x220px Workmesh banner

They should be of the same design, with minor adjustments to fit the dimensions indicated. As they are web components, 72dpi, RGB are standard requirements for the images.

Deliverables: 1 jpg of each type of banner. (3 in total)

Just a heads-up: The blipster and chatterly banners would be partially blocked by its user-icon as shown in the two attached guide illustrations. Please make sure that the banner designed take into consideration of this and do not put in anything important (e.g. logo) in those spots.
Updates

Reason: Deadline extended because more interests have been registered. Thanks, guys.

Target Market(s)

Professional project managers, CEOs, Directors, managers in other fields.

Industry/Entity Type

Media

Requirements
Must have
• The conference logo must be part of the design of the banner. Would be great if the design can relate well with the logo.
Nice to have
• If stock images are needed to develop this banner, please inform.

```html
<!DOCTYPE html>
<html lang="en">
<head>
<meta charset="utf-8">
<title>Shaping the Future – Conference Banner</title>
<link href="https://fonts.googleapis.com/css2?family=Fredoka:wght@500&family=Open+Sans:wght@400;600;700&display=swap" rel="stylesheet">
<style>
  :root {
    --page-bg: #3f3f3f;
    --band-blue: #0b41a8;
    --deep-blue: #0a3aa6;
    --sky-top: #3f6fb8;
    --sky-low: #8fb2dd;
    --tower-light: #d9dde3;
    --tower-tan: #b89a82;
    --tower-dark: #3b3f4a;
    --harbour-blue: #2a62c0;
    --title-light: #ffffff;
    --title-shade: #b4b8c2;
    --button-navy: #0f1d33;
    --arrow-cyan: #7fd3ff;
    --panel-white: #ffffff;
    --brand-blue: #0b41a8;
  }
  html, body {
    margin: 0;
    padding: 0;
    width: 1200px;
    height: 1000px;
    overflow: hidden;
    background: var(--page-bg);
  }
  .canvas {
    position: relative;
    width: 1200px;
    height: 1000px;
  }
  .banner {
    position: absolute;
    left: 12px;
    top: 310px;
    width: 1176px;
    height: 405px;
    overflow: hidden;
    box-shadow: 2px 3px 6px rgba(0,0,0,0.6);
  }
  .title-band {
    position: absolute;
    left: 0; top: 0;
    width: 100%;
    height: 85px;
    background: var(--band-blue);
    display: flex;
    align-items: center;
    justify-content: center;
  }
  .title-band h1 {
    margin: 0;
    font-family: "Fredoka", sans-serif;
    font-weight: 500;
    font-size: 64px;
    letter-spacing: 0.5px;
    word-spacing: 16px;
    line-height: 1;
    padding-bottom: 8px;
    background: linear-gradient(180deg, var(--title-light) 45%, var(--title-shade) 100%);
    -webkit-background-clip: text;
    background-clip: text;
    color: transparent;
    filter: drop-shadow(1px 3px 2px rgba(0,0,0,0.6));
  }
  .city-photo {
    position: absolute;
    left: 0; top: 85px;
    width: 100%;
    height: 320px;
    background:
      linear-gradient(90deg,
        rgba(217,221,227,0.55) 0%, rgba(59,63,74,0.55) 14%, rgba(217,221,227,0.5) 30%,
        rgba(59,63,74,0.35) 40%, rgba(217,221,227,0.6) 50%, rgba(217,221,227,0.45) 62%,
        rgba(184,154,130,0.6) 76%, rgba(184,154,130,0.5) 84%, rgba(90,60,50,0.55) 95%, rgba(90,60,50,0.5) 100%),
      linear-gradient(180deg, var(--sky-top) 0%, var(--sky-low) 40%, #a8b4c4 60%, #6f8aa8 76%, var(--harbour-blue) 100%);
    background-size: 100% 55%, 100% 100%;
    background-position: 0 58%, 0 0;
    background-repeat: no-repeat;
  }
  .bottom-wash {
    position: absolute;
    left: 0; bottom: 0;
    width: 100%;
    height: 130px;
  }
  .tagline {
    position: absolute;
    left: 186px;
    top: 343px;
    margin: 0;
    font-family: "Open Sans", sans-serif;
    font-size: 22.5px;
    font-weight: 400;
    color: #ffffff;
  }
  .join-button {
    position: absolute;
    left: 636px;
    top: 340px;
    width: 133px;
    height: 40px;
    border-radius: 5px;
    background: var(--button-navy);
    color: #ffffff;
    font-family: "Open Sans", sans-serif;
    font-weight: 600;
    font-size: 17px;
    letter-spacing: -0.5px;
    display: flex;
    align-items: center;
    justify-content: center;
    gap: 9px;
    text-decoration: none;
  }
  .join-button::before {
    content: "";
    border-left: 6px solid var(--arrow-cyan);
    border-top: 5px solid transparent;
    border-bottom: 5px solid transparent;
  }
  .logo-panel {
    position: absolute;
    left: 2px;
    top: 212px;
    width: 176px;
    height: 193px;
  }
  .logo-name {
    position: absolute;
    left: 2px;
    top: 232px;
    width: 176px;
    height: 160px;
    display: flex;
    flex-direction: column;
    align-items: center;
    justify-content: center;
    gap: 12px;
    font-family: "Open Sans", sans-serif;
    font-weight: 700;
    font-size: 32px;
    color: var(--brand-blue);
  }
  .logo-name .dot {
    width: 62px;
    height: 62px;
    border-radius: 50%;
    background: var(--brand-blue);
  }
</style>
</head>
<body>
<div class="canvas">
  <section class="banner">
    <header class="title-band">
      <h1>shaping the future</h1>
    </header>

    <div class="city-photo" role="img" aria-label="Photograph of a harbourside city skyline with high-rise towers, a marina with yacht masts and a blue sky with faint sparkles"></div>

    <svg class="bottom-wash" viewBox="0 0 1176 130" preserveAspectRatio="none" aria-hidden="true">
      <defs>
        <linearGradient id="washFill" x1="0" y1="0" x2="0" y2="1">
          <stop offset="0" stop-color="#0a3aa6" stop-opacity="0"/>
          <stop offset="0.45" stop-color="#0a3aa6" stop-opacity="0.7"/>
          <stop offset="1" stop-color="#0a3aa6" stop-opacity="1"/>
        </linearGradient>
      </defs>
      <rect x="0" y="0" width="1176" height="130" fill="url(#washFill)"/>
      <path d="M160 110 Q420 60 640 95 T1176 80" fill="none" stroke="#ffffff" stroke-opacity="0.18" stroke-width="3"/>
      <path d="M160 125 Q460 85 700 112 T1176 100" fill="none" stroke="#ffffff" stroke-opacity="0.12" stroke-width="2"/>
    </svg>

    <svg class="logo-panel" viewBox="0 0 176 193" aria-hidden="true">
      <path d="M0 0 Q90 10 176 40 L176 178 Q90 185 0 193 Z" fill="#ffffff"/>
    </svg>
    <div class="logo-name"><span class="dot"></span>ZRV.org</div>

    <p class="tagline">21st project management conference</p>
    <a class="join-button" href="#">JOIN NOW</a>
  </section>
</div>
</body>
</html>
```